Brell Harbor Company Business Cards

Front and Back Business Card - logo and text setup - cool design. I need workable photoshop or illustrator files so I can setup each employee card with design that is created
Updates

Hi everyone, thank you for the great entries. Please no more white and blue cards - there are so many already - black and silver only now please. thanks!

Target Market(s)

Construction Industry - Facility Managers

Industry/Entity Type

Construction

Contact Information for Business Card

I really like contemporary simplistic looks - clean neat....not opposed to seeing some black backrounds

Requirements
Must have
• Logo/website address with design on front only - www.brellharbor-example.com (logo attached)
• Back:
• Name/Title/Company Address/Phone/email address
Nice to have
• Cool design
Should not have
• Nothing gimmicky like Fire or Water - since we are a Fire Protection company - it has all been done

```html
<!DOCTYPE html>
<html lang="en">
<head>
<meta charset="utf-8">
<title>Brell Harbor Company – Business Cards</title>
<link rel="stylesheet" href="https://fonts.googleapis.com/css2?family=Arimo:wght@700&family=Crimson+Text:wght@400;600&display=swap">
<style>
  :root {
    --backdrop: #262626;
    --card: #151515;
    --card-edge: #2e2e2e;
    --accent: #e4553a;
    --wordmark: #e8775c;
    --ink: #f2f2f2;
    --ink-soft: #d9d9d9;
  }
  * { box-sizing: border-box; margin: 0; padding: 0; }
  html, body {
    width: 1200px;
    height: 800px;
    overflow: hidden;
    background: var(--backdrop);
  }
  .sheet {
    position: relative;
    width: 1200px;
    height: 800px;
    display: flex;
    justify-content: center;
    align-items: center;
    gap: 60px;
  }
  .card {
    position: relative;
    width: 340px;
    height: 580px;
    background: linear-gradient(180deg, #1b1b1b 0%, var(--card) 100%);
    border: 1px solid var(--card-edge);
    border-radius: 4px;
    display: flex;
    flex-direction: column;
    align-items: center;
    text-align: center;
    font-family: "Crimson Text", Georgia, serif;
    color: var(--ink);
  }
  .wordmark {
    font-family: "Arimo", Arial, sans-serif;
    font-weight: 700;
    color: var(--wordmark);
    letter-spacing: -0.5px;
    line-height: 1;
  }
  /* contact side */
  .card--contact { padding-top: 78px; }
  .card--contact .wordmark { font-size: 34px; }
  .person-name {
    margin-top: 78px;
    font-family: "Arimo", Arial, sans-serif;
    font-weight: 700;
    font-size: 20px;
    letter-spacing: 0.5px;
    color: var(--accent);
  }
  .person-title {
    margin-top: 6px;
    font-size: 16px;
    letter-spacing: 0.4px;
    color: var(--ink-soft);
  }
  .icon-rule {
    margin-top: 16px;
    display: flex;
    align-items: center;
    gap: 8px;
  }
  .icon-rule .rule {
    width: 44px;
    height: 1px;
    background: var(--accent);
  }
  .icon-rule svg { display: block; }
  .contact-list {
    margin-top: 12px;
    list-style: none;
    font-size: 16px;
    line-height: 1.4;
    letter-spacing: 0.4px;
  }
  .accent { color: var(--accent); }
  .divider {
    margin-top: 16px;
    width: 150px;
    height: 1px;
    background: var(--accent);
  }
  .company-name {
    margin-top: 16px;
    font-size: 16px;
    letter-spacing: 0.4px;
    color: var(--accent);
  }
  .address {
    margin-top: 4px;
    font-style: normal;
    font-size: 16px;
    line-height: 1.4;
    letter-spacing: 0.4px;
  }
  /* logo side */
  .card--logo { justify-content: space-between; padding: 190px 0 120px; }
  .card--logo .wordmark { font-size: 38px; }
  .card--logo .website { font-size: 17px; letter-spacing: 0.6px; }
</style>
</head>
<body>
<main class="sheet">
  <section class="card card--contact" aria-label="Contact side">
    <div class="wordmark">brell harbor inc.</div>
    <h1 class="person-name">DANA WHITLOCK</h1>
    <p class="person-title">Senior Consultant</p>
    <div class="icon-rule">
      <span class="rule"></span>
      <svg width="16" height="16" viewBox="0 0 16 16" aria-label="Phone">
        <circle cx="8" cy="8" r="8" fill="var(--accent)"/>
        <path d="M5.3 4.2l1.3 1.5-.6 1c.5 1 1.3 1.8 2.3 2.3l1-.6 1.5 1.3-.7 1.2C7.8 11.2 4.8 8.2 4.1 5l1.2-.8z" fill="#151515"/>
      </svg>
      <svg width="16" height="16" viewBox="0 0 16 16" aria-label="Email">
        <circle cx="8" cy="8" r="8" fill="var(--accent)"/>
        <rect x="4.3" y="5.3" width="7.4" height="5.4" fill="none" stroke="#151515" stroke-width="1"/>
        <path d="M4.3 5.3L8 8.3l3.7-3" fill="none" stroke="#151515" stroke-width="1"/>
      </svg>
      <svg width="16" height="16" viewBox="0 0 16 16" aria-label="Website">
        <circle cx="8" cy="8" r="8" fill="var(--accent)"/>
        <circle cx="8" cy="8" r="4" fill="none" stroke="#151515" stroke-width="0.9"/>
        <ellipse cx="8" cy="8" rx="1.7" ry="4" fill="none" stroke="#151515" stroke-width="0.9"/>
        <path d="M4 8h8" stroke="#151515" stroke-width="0.9"/>
      </svg>
      <span class="rule"></span>
    </div>
    <ul class="contact-list">
      <li>555.014.2290</li>
      <li>info@brellharbor-example.com</li>
      <li>www.<span class="accent">brellharbor-example</span>.com</li>
    </ul>
    <div class="divider"></div>
    <p class="company-name">brell harbor inc.</p>
    <address class="address">48 Lantern Works<br>Drive Harlow Bay, NY 10000</address>
  </section>

  <section class="card card--logo" aria-label="Logo side">
    <div class="wordmark">brell harbor inc.</div>
    <p class="website">www.<span class="accent">brellharbor-example</span>.com</p>
  </section>
</main>
</body>
</html>
```